Compass & Canvas needs new business card design

I need a new business card design. I'm looking for out-of-the-box design which represents the freedom of being a location independent entrepreneur.
I offer coaching, retreats and trips.
I would like to see designs with and without the photo.
Colors I use are black (#000000), green (#25A796) and brown (#D7C38C)
Website compassandcanvas.net

Target Market(s)

location independent entrepreneurs, digital nomads, people looking to swap the 9 to 5 for a lifestyle business

Industry/Entity Type

Business

Contact Information for Business Card

Daria Tolsen
Your Lifestyle Business Coach, Retreat & Trip Leader
http://compassandcanvas.net
hello@compassandcanvas.net
Live a life you don't need a holiday from

Font styles to use
Serif
Sans Serif

Requirements
Must have
• One side should contain only the logo. I would also consider having the "Live a life you don't need a holiday from" on that side too (depending on how it looks)
• Please show both sides on the designs.

```html
<!DOCTYPE html>
<html lang="en">
<head>
<meta charset="utf-8">
<title>Compass &amp; Canvas — Business Card</title>
<link rel="stylesheet" href="https://fonts.googleapis.com/css2?family=Oswald:wght@300;400;500&display=swap">
<style>
  :root {
    --ink: #000000;
    --teal: #25A796;
    --sand: #D7C38C;
    --sand-soft: rgba(215, 195, 140, 0.35);
    --paper: #ffffff;
    --backdrop: #e9f0d8;
    --sky: #d7edf3;
    --foliage: #8f9470;
    --bark: #9a9a92;
  }
  * { margin: 0; padding: 0; box-sizing: border-box; }
  html, body {
    width: 1200px;
    height: 1200px;
    overflow: hidden;
    background: var(--backdrop);
    font-family: "Oswald", "Arial Narrow", sans-serif;
  }
  .canvas {
    position: relative;
    width: 1200px;
    height: 1200px;
  }
  .card {
    position: absolute;
    left: 218px;
    width: 778px;
    height: 452px;
    background: var(--paper);
    overflow: hidden;
  }
  /* Front: logo side */
  .card--front { top: 41px; }
  .logo-band {
    position: absolute;
    left: 0;
    top: 90px;
    width: 100%;
    height: 283px;
    background: var(--sand);
    display: flex;
    align-items: center;
    justify-content: center;
  }
  .logo-name {
    font-weight: 500;
    font-size: 86px;
    letter-spacing: 2px;
    text-transform: uppercase;
    color: var(--ink);
    line-height: 1;
  }
  /* Back: contact side */
  .card--back {
    top: 619px;
    background: linear-gradient(to right, var(--foliage) 0%, #b5b89a 35%, var(--sky) 72%, var(--paper) 100%);
  }
  .portrait {
    position: absolute;
    left: 0;
    top: 0;
    width: 62%;
    height: 100%;
    background:
      linear-gradient(to right, rgba(154,154,146,0) 60%, rgba(215,237,243,0.9) 100%),
      linear-gradient(to bottom, var(--bark) 0%, #8d9a6a 25%, #a9a46c 60%, var(--bark) 88%);
  }
  .name {
    position: absolute;
    right: 42px;
    top: 38px;
    font-weight: 500;
    font-size: 32px;
    color: var(--teal);
    letter-spacing: 0.5px;
  }
  .info-band {
    position: absolute;
    left: 0;
    top: 91px;
    width: 100%;
    height: 282px;
    background: linear-gradient(to right, var(--sand-soft) 0%, rgba(215,195,140,0.75) 45%, var(--sand) 70%);
    color: var(--paper);
    text-align: right;
    padding: 36px 42px 0 0;
    font-weight: 300;
    font-size: 27px;
    line-height: 40px;
  }
  .info-band .role { display: block; }
  .info-band .contact { display: block; margin-top: 40px; }
  .tagline-strip {
    position: absolute;
    left: 0;
    top: 373px;
    width: 100%;
    height: 79px;
    background: linear-gradient(to right, rgba(255,255,255,0) 0%, rgba(255,255,255,0.7) 45%, var(--paper) 65%);
    display: flex;
    align-items: center;
    justify-content: flex-end;
    padding-right: 42px;
  }
  .tagline {
    font-weight: 400;
    font-size: 26px;
    color: var(--teal);
  }
</style>
</head>
<body>
<div class="canvas">
  <section class="card card--front">
    <div class="logo-band">
      <span class="logo-name">Compass &amp; Canvas</span>
    </div>
  </section>

  <section class="card card--back">
    <div class="portrait" role="img" aria-label="Photo of the coach sitting among trees, holding a wooden sign"></div>
    <h1 class="name">Daria Tolsen</h1>
    <div class="info-band">
      <span class="role">Your Lifestyle Business Coach</span>
      <span class="role">Retreat &amp; Trip Leader</span>
      <span class="contact">http://compassandcanvas.net<br>hello@compassandcanvas.net</span>
    </div>
    <div class="tagline-strip">
      <p class="tagline">Live a life you don't need a holiday from</p>
    </div>
  </section>
</div>
</body>
</html>
```